Business Card Design Project

I am looking for a double sided business card design that is bold on one side with creative use of the logo, but clean and professional looking on the other side with the contact information provided.

Target Market(s)

My target market is recruitment agents, senior managers of multinational companies. The target segments are finance and I.T.

Industry/Entity Type

Business

Requirements
Must have
• Double sided. Use provided logo.

Information to include, but use your creativity for the tags (example):
Name (Marcus Feldane)
Position (Director)
Mobile (+44 7XXXXXXXXX)
Phone (+44 20XXXXXXXX)
Email (marcus@wendlebymarsh.com)
Website (www.wendlebymarsh.com)

```html
<!DOCTYPE html>
<html lang="en">
<head>
<meta charset="utf-8">
<title>Wendleby Marsh Consulting Limited – Business Card</title>
<link href="https://fonts.googleapis.com/css2?family=Open+Sans:wght@400;600&display=swap" rel="stylesheet">
<style>
  :root {
    --backdrop: #35363a;
    --card: #ffffff;
    --ink: #3a3a3a;
    --ink-soft: #555555;
    --brand-blue: #1f6fb8;
    --brand-green: #9cc63b;
    --rule: #8a8a8a;
  }
  * { box-sizing: border-box; margin: 0; padding: 0; }
  html, body {
    width: 1200px; height: 800px; overflow: hidden;
    background: var(--backdrop);
    font-family: "Open Sans", Arial, sans-serif;
  }
  .sheet {
    width: 1200px; height: 800px;
    display: flex; align-items: center; justify-content: center; gap: 40px;
  }
  .card {
    position: relative;
    width: 540px; height: 310px;
    background: var(--card);
    overflow: hidden;
  }

  /* brand lockup: invented name in one colour and weight, one plain circle */
  .brand { display: flex; align-items: center; gap: 12px; }
  .brand__dot { border-radius: 50%; background: var(--brand-green); flex: none; }
  .brand__name {
    color: var(--brand-blue); font-weight: 600; text-transform: uppercase;
    line-height: 1.15; letter-spacing: 0.02em; white-space: nowrap;
  }

  /* front: contact side */
  .card--front .brand { position: absolute; left: 36px; top: 44px; }
  .card--front .brand__dot { width: 40px; height: 40px; }
  .card--front .brand__name { font-size: 15px; }

  .person {
    position: absolute; left: 290px; right: 24px; top: 148px;
    text-align: center;
  }
  .person__name { font-size: 21px; font-weight: 600; color: var(--ink); white-space: nowrap; }
  .person__rule { height: 1px; background: var(--rule); margin: 3px 0 2px; }
  .person__role { font-size: 10px; color: var(--brand-blue); }

  .contact {
    position: absolute; left: 200px; right: 20px; top: 222px;
    border-top: 1px solid var(--rule);
    padding-top: 10px;
    display: flex;
  }
  .contact__col {
    list-style: none; display: flex; flex-direction: column; gap: 6px; flex: none;
  }
  .contact__col--left { padding: 0 12px 0 16px; border-right: 1px solid var(--rule); }
  .contact__col--right { padding-left: 10px; }
  .contact__item {
    display: flex; align-items: center; gap: 7px;
    font-size: 10.5px; color: var(--ink-soft); line-height: 14px;
    white-space: nowrap;
  }
  .contact__icon { width: 12px; height: 12px; flex: none; fill: var(--brand-blue); }

  /* back: bold brand side */
  .card--back { display: flex; align-items: center; justify-content: center; }
  .card--back .brand { gap: 18px; }
  .card--back .brand__dot { width: 74px; height: 74px; }
  .card--back .brand__name { font-size: 26px; }
</style>
</head>
<body>
<main class="sheet">

  <section class="card card--front" aria-label="Business card front">
    <div class="brand">
      <span class="brand__dot" aria-hidden="true"></span>
      <p class="brand__name">Wendleby Marsh<br>Consulting Limited</p>
    </div>

    <div class="person">
      <h1 class="person__name">Marcus Feldane</h1>
      <div class="person__rule"></div>
      <p class="person__role">Director</p>
    </div>

    <div class="contact">
      <ul class="contact__col contact__col--left">
        <li class="contact__item">
          <svg class="contact__icon" viewBox="0 0 12 12" aria-hidden="true"><path d="M6 0a4 4 0 0 0-4 4c0 3 4 8 4 8s4-5 4-8a4 4 0 0 0-4-4zm0 5.6A1.6 1.6 0 1 1 6 2.4a1.6 1.6 0 0 1 0 3.2z"/></svg>
          address goes here
        </li>
        <li class="contact__item">
          <svg class="contact__icon" viewBox="0 0 12 12" aria-hidden="true"><path d="M2.4 0.6 4.2 2.6 3.2 4.2c.7 1.6 2 2.9 3.6 3.6l1.6-1 2 1.8-.9 2.3C5 10.6 1.2 6.8.6 1.5z"/></svg>
          +44 7XXXXXXXXX
        </li>
        <li class="contact__item">
          <svg class="contact__icon" viewBox="0 0 12 12" aria-hidden="true"><path d="M2.4 0.6 4.2 2.6 3.2 4.2c.7 1.6 2 2.9 3.6 3.6l1.6-1 2 1.8-.9 2.3C5 10.6 1.2 6.8.6 1.5z"/></svg>
          +44 20XXXXXXXX
        </li>
      </ul>
      <ul class="contact__col contact__col--right">
        <li class="contact__item">
          <svg class="contact__icon" viewBox="0 0 12 12" aria-hidden="true"><path fill-rule="evenodd" d="M6 0a6 6 0 1 1 0 12A6 6 0 0 1 6 0zm0 1.2a4.8 4.8 0 1 0 0 9.6 4.8 4.8 0 0 0 0-9.6zM5.4 1.5h1.2v9H5.4zM1.5 5.4h9v1.2h-9z"/></svg>
          www.wendlebymarsh.com
        </li>
        <li class="contact__item">
          <svg class="contact__icon" viewBox="0 0 12 12" aria-hidden="true"><path d="M0 2h12v1L6 7 0 3zM0 4.4l6 4 6-4V10H0z"/></svg>
          marcus@wendlebymarsh.com
        </li>
      </ul>
    </div>
  </section>

  <section class="card card--back" aria-label="Business card back">
    <div class="brand">
      <span class="brand__dot" aria-hidden="true"></span>
      <p class="brand__name">Wendleby Marsh<br>Consulting Limited</p>
    </div>
  </section>

</main>
</body>
</html>
```